The Merchant Crossroads Book Cover

I need a Book Cover Design for a new book:
Title - "The Merchant Crossroads"
Subtitle - "Lessons No Classroom Ever Gave Me"
Author - "Darren Whitlock"

Target Market(s)

Entrepreneur's and Small Business Owners

Industry/Entity Type

Entrepreneur

Font styles to use
Sans Serif

Requirements
Must have
• The branding colors should match our website (Black and accent color: #FBBC05)
• http://MerchantCrossroadsBook.example
• Secondary Subtile (top bar) on front of cover - "A Documentary"
• Back Cover: Brief description, author photo, and the ISBN Number
Nice to have
• A Detour Sign with the word "Detour" on it (or a sign with a "squiggly" line example) ... or a type of image that is on the bottom of Home page of website (road in wilderness).

```html
<!DOCTYPE html>
<html lang="en">
<head>
<meta charset="utf-8">
<title>The Merchant Crossroads — Book Cover</title>
<link rel="stylesheet" href="https://fonts.googleapis.com/css2?family=Bebas+Neue&family=Barlow+Semi+Condensed:wght@600&display=swap">
<style>
  :root {
    --accent: #FBBC05;
    --title-white: #ffffff;
    --ink-teal: #1f3d4d;
    --sky-top: #527f93;
    --sky-mid: #8fb3c0;
    --horizon: #d3e2e4;
    --sand: #cdbd9f;
    --road-dark: #5c5148;
  }
  html, body {
    margin: 0;
    padding: 0;
    overflow: hidden;
    background: #ffffff;
  }
  .cover {
    position: relative;
    width: 778px;
    height: 1200px;
    overflow: hidden;
    font-family: "Bebas Neue", "Arial Narrow", sans-serif;
  }
  .cover-scene {
    position: absolute;
    inset: 0;
    background: linear-gradient(
      to bottom,
      var(--sky-top) 0%,
      var(--sky-mid) 35%,
      var(--horizon) 56%,
      var(--sand) 61%,
      #b9a88c 78%,
      var(--road-dark) 100%
    );
  }
  .cover-text {
    position: absolute;
    inset: 0;
    text-align: center;
  }
  .series-label {
    position: absolute;
    top: 52px;
    left: 0;
    right: 0;
    margin: 0;
    font-family: "Barlow Semi Condensed", "Arial Narrow", sans-serif;
    font-weight: 600;
    font-size: 28px;
    color: var(--ink-teal);
  }
  .book-title {
    margin: 0;
    font-weight: 400;
    line-height: 1;
  }
  .title-the {
    position: absolute;
    top: 150px;
    left: 0;
    right: 0;
    font-size: 62px;
    color: var(--title-white);
    opacity: 0.9;
  }
  .title-lead {
    position: absolute;
    top: 212px;
    left: 0;
    right: 0;
    font-size: 104px;
    color: var(--accent);
    letter-spacing: 1px;
  }
  .title-main {
    position: absolute;
    top: 310px;
    left: 0;
    right: 0;
    font-size: 150px;
    color: var(--title-white);
    letter-spacing: 1px;
  }
  .subtitle {
    position: absolute;
    top: 488px;
    left: 120px;
    right: 120px;
    margin: 0;
    font-family: "Barlow Semi Condensed", "Arial Narrow", sans-serif;
    font-weight: 600;
    font-size: 34px;
    line-height: 1.3;
    color: var(--ink-teal);
  }
  .author {
    position: absolute;
    top: 1108px;
    left: 0;
    right: 0;
    margin: 0;
    font-size: 64px;
    font-weight: 400;
    letter-spacing: 2px;
    color: var(--title-white);
  }
</style>
</head>
<body>
  <main class="cover">
    <div class="cover-scene" role="img" aria-label="Photograph of a straight two-lane desert highway stretching to distant mountains under a pale blue sky"></div>
    <div class="cover-text">
      <p class="series-label">A Documentary</p>
      <h1 class="book-title">
        <span class="title-the">THE</span>
        <span class="title-lead">MERCHANT</span>
        <span class="title-main">CROSSROADS</span>
      </h1>
      <p class="subtitle">Lessons No Classroom Ever Gave Me</p>
      <p class="author">Darren Whitlock</p>
    </div>
  </main>
</body>
</html>
```